Creative & Professional Business Card for hair salon

We are looking to update our business cards. Our salon is creative, modern, progressive and professional and looking for a design that will reflect this.

```html
<!DOCTYPE html>
<html lang="en">
<head>
<meta charset="utf-8">
<title>Silver Mist Studio – Business Cards</title>
<link href="https://fonts.googleapis.com/css2?family=Arimo:wght@400;700&family=Raleway:wght@300&display=swap" rel="stylesheet">
<style>
  :root {
    --bg: #e9e7e4;
    --card-white: #ffffff;
    --card-black: #111214;
    --brand-blue: #4f7d9e;
    --brand-teal: #7fb2c2;
    --rule: #9fb6c6;
    --text-grey: #3f3f42;
    --silver: #d6d8da;
  }
  * { margin: 0; padding: 0; box-sizing: border-box; }
  html, body { width: 745px; height: 1200px; overflow: hidden; }
  body { background: var(--bg); font-family: "Arimo", Arial, sans-serif; }

  .sheet { position: relative; width: 745px; height: 1200px; }
  .card-set { position: absolute; left: 0; width: 745px; height: 600px; }
  .card-set--first { top: 0; }
  .card-set--second { top: 600px; }

  .card {
    position: absolute;
    top: 196px;
    width: 340px;
    height: 208px;
    box-shadow: 0 6px 18px rgba(0,0,0,0.18);
  }
  .card--front { left: 22px; background: var(--card-white); }
  .card--back { left: 383px; background: var(--card-black); display: flex; align-items: center; justify-content: center; }

  .brand-name {
    position: absolute;
    left: 60px;
    top: 34px;
    font-family: "Raleway", sans-serif;
    font-weight: 300;
    font-size: 25px;
    color: var(--brand-blue);
    letter-spacing: 0.3px;
  }
  .brand-name--back { position: static; color: var(--silver); font-size: 27px; }

  .divider {
    position: absolute;
    left: 24px;
    right: 22px;
    top: 88px;
    height: 1px;
    background: var(--rule);
  }

  .contact-list {
    position: absolute;
    right: 16px;
    top: 98px;
    list-style: none;
    text-align: right;
    font-size: 8.6px;
    line-height: 13px;
    color: var(--text-grey);
  }
  .contact-list li { display: flex; justify-content: flex-end; align-items: center; gap: 5px; }
  .contact-icon { width: 8px; height: 8px; flex: none; }

  .person {
    position: absolute;
    left: 26px;
    top: 140px;
    color: var(--text-grey);
  }
  .person-name { font-size: 14px; font-weight: 700; color: var(--brand-blue); line-height: 16px; }
  .person-role { font-size: 9.5px; color: var(--brand-teal); line-height: 12px; }
  .person-address { font-size: 8.6px; line-height: 12px; margin-top: 2px; }

  .footer-band { position: absolute; left: 0; bottom: 0; width: 340px; height: 16px; }
</style>
</head>
<body>
<main class="sheet">

  <section class="card-set card-set--first">
    <article class="card card--front">
      <div class="brand-name">Silver Mist Studio</div>
      <div class="divider"></div>
      <ul class="contact-list">
        <li>07 5550 1234
          <svg class="contact-icon" viewBox="0 0 10 10"><path d="M2 1 L4 1 L4.8 3.2 L3.6 4 Q4.6 5.8 6 6.4 L6.8 5.2 L9 6 L9 8 Q9 9 8 9 Q1 8.4 1 2 Q1 1 2 1 Z" fill="var(--brand-blue)"/></svg></li>
        <li>hello@silvermiststudio.com.au
          <svg class="contact-icon" viewBox="0 0 10 10"><rect x="0.5" y="2" width="9" height="6.5" fill="var(--brand-blue)"/><path d="M0.5 2 L5 5.8 L9.5 2" stroke="#fff" stroke-width="0.9" fill="none"/></svg></li>
        <li>SilverMistbyDanaWhitlow
          <svg class="contact-icon" viewBox="0 0 10 10"><circle cx="5" cy="5" r="4.5" fill="var(--brand-blue)"/></svg></li>
        <li>www.silvermiststudio.com.au
          <svg class="contact-icon" viewBox="0 0 10 10"><circle cx="5" cy="5" r="4.5" fill="var(--brand-blue)"/></svg></li>
      </ul>
      <div class="person">
        <p class="person-name">Luca Benetti</p>
        <p class="person-address">5/22 Palmer Lane<br>Kinsale</p>
      </div>
      <svg class="footer-band" viewBox="0 0 340 16" preserveAspectRatio="none">
        <defs>
          <linearGradient id="band-a" x1="0" x2="1"><stop offset="0" stop-color="var(--brand-teal)"/><stop offset="1" stop-color="var(--brand-blue)"/></linearGradient>
        </defs>
        <path d="M0 11 L196 11 L204 4 L340 4 L340 16 L0 16 Z" fill="url(#band-a)"/>
        <path d="M0 8 L192 8 L200 1 L340 1" stroke="var(--brand-blue)" stroke-width="0.8" fill="none"/>
      </svg>
    </article>
    <article class="card card--back">
      <div class="brand-name brand-name--back">Silver Mist Studio</div>
    </article>
  </section>

  <section class="card-set card-set--second">
    <article class="card card--front">
      <div class="brand-name">Silver Mist Studio</div>
      <div class="divider"></div>
      <ul class="contact-list">
        <li>07 5550 1234
          <svg class="contact-icon" viewBox="0 0 10 10"><path d="M2 1 L4 1 L4.8 3.2 L3.6 4 Q4.6 5.8 6 6.4 L6.8 5.2 L9 6 L9 8 Q9 9 8 9 Q1 8.4 1 2 Q1 1 2 1 Z" fill="var(--brand-blue)"/></svg></li>
        <li>hello@silvermiststudio.com.au
          <svg class="contact-icon" viewBox="0 0 10 10"><rect x="0.5" y="2" width="9" height="6.5" fill="var(--brand-blue)"/><path d="M0.5 2 L5 5.8 L9.5 2" stroke="#fff" stroke-width="0.9" fill="none"/></svg></li>
        <li>SilverMistbyDanaWhitlow
          <svg class="contact-icon" viewBox="0 0 10 10"><circle cx="5" cy="5" r="4.5" fill="var(--brand-blue)"/></svg></li>
        <li>www.silvermiststudio.com.au
          <svg class="contact-icon" viewBox="0 0 10 10"><circle cx="5" cy="5" r="4.5" fill="var(--brand-blue)"/></svg></li>
      </ul>
      <div class="person">
        <p class="person-name">Dana Whitlow</p>
        <p class="person-role">Director / Founder</p>
        <p class="person-address">5/22 Palmer Lane<br>Kinsale</p>
      </div>
      <svg class="footer-band" viewBox="0 0 340 16" preserveAspectRatio="none">
        <defs>
          <linearGradient id="band-b" x1="0" x2="1"><stop offset="0" stop-color="var(--brand-teal)"/><stop offset="1" stop-color="var(--brand-blue)"/></linearGradient>
        </defs>
        <path d="M0 11 L196 11 L204 4 L340 4 L340 16 L0 16 Z" fill="url(#band-b)"/>
        <path d="M0 8 L192 8 L200 1 L340 1" stroke="var(--brand-blue)" stroke-width="0.8" fill="none"/>
      </svg>
    </article>
    <article class="card card--back">
      <div class="brand-name brand-name--back">Silver Mist Studio</div>
    </article>
  </section>

</main>
</body>
</html>
```